A wordpress website for the coolest Resort App

We have developed a mobile app - Zorbo and we want to develop a cool, neat and simple wordpress website for it.

I have attached the basics in a keynote/ ppt - but i need you to bring it more to life. plus there are additions:

FOr the number of pages, we will have:
1- Home: very similar to the one pager
2- How it works: Showing step by step on how the app works, and how it connects to the POS system of the restaurant etc with spanshots from the app
3- Benefit: Elaborating more on each of the benefits that is mentioned in the ONE PAGE document, with additional statistics, reference etc.. and embedded videos and animation
4- who we are page
5- In the press page: links to the articles where zorbo was mentioned
6- Get in touch page
7- FAQ
Updates

Target Market(s)

Resorts, hotels, beach and pool restaurant operators

Industry/Entity Type

Hospitality

Coding

Coded - Design and coding required

Font styles to use
Other font styles liked:
• I have attached the fonts i want to use: ROboto is the main font

Colors

Designer to choose colors to be used in the design.

Requirements
Must have
• Logo, icons for each benefit, you can also use the mood picture i attached or any other picture you recommend - maybe just something related to the app
• I also attached the Main colour, the orange and the blue is the accent one
• I attached the fonts, roboto is the main one
• there should also be a contact us:
• Email : info@zorboapp-mail.com
• Mobile: +971 5 23 47 90 18
• Address: Palm Quarter - Dubai - United Arab Emirates

```html
<!DOCTYPE html>
<html lang="en">
<head>
<meta charset="utf-8">
<title>Zorbo – Resort App</title>
<link rel="stylesheet" href="https://fonts.googleapis.com/css2?family=Roboto:wght@400;500;700&family=Asap:wght@400;500;700&display=swap">
<style>
:root{
  --orange:#fc7d4b;
  --blue:#2e9ed6;
  --dark:#333333;
  --ink:#222222;
  --text:#555555;
  --white:#ffffff;
  --night:#1d2430;
}
*{margin:0;padding:0;box-sizing:border-box}
html,body{width:1200px;height:3586px;overflow:hidden}
body{position:relative;background:var(--white);font-family:"Roboto",Arial,sans-serif;color:var(--text)}
.abs{position:absolute}
.heading{font-family:"Asap","Roboto",sans-serif;font-weight:400}
.accent{color:var(--orange)}

/* hero */
.hero-bg{position:absolute;left:0;top:0;width:1200px;height:700px}
.nav{left:79px;top:0;width:1040px;height:115px;background:rgba(225,228,232,.55)}
.nav a{position:absolute;top:40px;font-size:20px;color:var(--white);text-decoration:none}
.brand{position:absolute;display:flex;align-items:center;gap:14px;font-family:"Roboto",sans-serif;font-weight:700}
.brand-dot{border-radius:50%;background:var(--orange)}
.hero-title{left:0;top:268px;width:1200px;text-align:center;font-size:48px;color:var(--white);letter-spacing:1px}
.hero-sub{left:285px;top:334px;width:630px;text-align:center;font-size:17px;line-height:24px;color:var(--white)}
.btn{position:absolute;height:56px;border-radius:28px;display:flex;align-items:center;font-size:21px;color:var(--white);text-transform:uppercase;white-space:nowrap}
.btn-ghost{left:382px;top:404px;width:206px;border:2px solid var(--white);justify-content:center}
.btn-solid{background:var(--orange);padding:0 4px 0 20px;justify-content:space-between}
.btn-arrow{flex:none;width:48px;height:48px;border-radius:50%;background:var(--white);display:flex;align-items:center;justify-content:center}
.swatch{position:absolute;left:1009px;width:83px;height:40px}

/* welcome */
.welcome-title{left:79px;top:732px;font-size:37px;color:var(--ink)}
.welcome-text{left:79px;top:800px;width:585px;font-size:14.4px;line-height:23.5px;color:var(--text)}
.video{left:686px;top:736px;width:435px;height:316px}
.play{left:874px;top:861px;width:62px;height:62px;border:4px solid var(--white);border-radius:50%}

/* benefit */
.benefit-title{left:700px;top:1212px;font-size:34px;color:var(--ink)}
.benefit-list{left:700px;top:1274px;list-style:none}
.benefit-list li{height:42px;display:flex;align-items:center;gap:16px;font-size:17px;color:var(--white);text-transform:uppercase;white-space:nowrap}
.benefit-list li.mixed{text-transform:none}

/* how it works */
.how-bg{left:0;top:1745px;width:1200px;height:956px}
.how-title{left:0;top:1770px;width:1200px;text-align:center;font-size:36px;color:var(--white);font-weight:500}
.step-box{position:absolute;width:155px;height:155px;background:var(--blue);display:flex;align-items:center;justify-content:center}
.step-text{position:absolute;width:260px;color:var(--white)}
.step-text h3{font-family:"Asap",sans-serif;font-size:20px;font-weight:700;color:var(--orange);margin-bottom:8px}
.step-text p{font-size:15.5px;line-height:23px}
.step-text.right{text-align:right}

/* news */
.news-title{left:0;top:2756px;width:1200px;text-align:center;font-size:40px;color:var(--ink)}
.news-card{position:absolute;top:2868px;width:333px}
.news-img{width:333px;height:167px}
.news-date{position:absolute;left:0;top:175px;width:53px;height:76px;background:var(--blue);color:var(--white);text-align:center;font-size:26px;line-height:36px;padding-top:2px}
.news-head{position:absolute;left:74px;top:175px;width:255px;font-size:16px;line-height:22px;font-weight:700;color:var(--ink)}
.news-body{position:absolute;left:74px;top:222px;width:255px;font-size:14.5px;line-height:22px;color:var(--text)}

/* footer */
.footer{left:0;top:3210px;width:1200px;height:308px;background:var(--dark)}
.foot-head{position:absolute;top:3250px;font-family:"Asap",sans-serif;font-size:20px;color:var(--white);padding-bottom:10px;border-bottom:1px solid #8a8a8a}
.foot-links{left:79px;top:3302px;list-style:none}
.foot-links li{font-size:14.5px;line-height:28.5px;color:var(--white)}
.divider{position:absolute;top:3300px;width:1px;height:178px;background:#5a5a5a}
.contact-row{position:absolute;left:298px;display:flex;gap:16px;font-size:14.5px;line-height:21px;color:var(--white)}
.field{position:absolute;left:607px;width:249px;height:37px;background:var(--white);border-radius:3px;font-size:12px;color:#777;padding:11px 10px}
.submit{left:607px;top:3444px;width:84px;height:36px;background:var(--blue);color:var(--white);font-size:20px;text-align:center;line-height:36px}
.social{position:absolute;top:3391px;width:43px;height:43px;background:#2f6bb5;border:2px solid var(--white)}
.copyright{left:0;top:3518px;width:1200px;height:68px;background:var(--orange);color:var(--white);font-size:14px;text-align:center;line-height:68px}
</style>
</head>
<body>

<!-- hero -->
<svg class="hero-bg" viewBox="0 0 1200 700" width="1200" height="700" role="img" aria-label="Resort beach with umbrellas and sun loungers by the sea">
  <defs>
    <linearGradient id="heroGrad" x1="0" y1="0" x2="0" y2="1">
      <stop offset="0" stop-color="#6f8ea3"/>
      <stop offset=".4" stop-color="#4f6c7c"/>
      <stop offset=".7" stop-color="#6c6154"/>
      <stop offset="1" stop-color="#3b3632"/>
    </linearGradient>
  </defs>
  <polygon points="0,0 1200,0 1200,655 0,600" fill="url(#heroGrad)"/>
  <polygon points="0,600 1200,655 1200,690 0,640" fill="#fc7d4b"/>
</svg>

<div class="abs nav">
  <a style="left:29px">Home</a>
  <a style="left:131px">How it works</a>
  <a style="left:294px">Benefit</a>
  <div class="brand" style="left:392px;top:26px;font-size:56px;color:#2b2b2b">
    <span class="brand-dot" style="width:54px;height:54px"></span><span>zorbo</span>
  </div>
  <a style="left:705px">who we are</a>
  <a style="left:861px">Faq</a>
  <a style="left:949px">Contact</a>
</div>

<h1 class="abs hero-title heading">MAKE YOUR HOLIDAY TRIP HERE</h1>
<p class="abs hero-sub">Lorem Ipsum is simply dummy text of the printing and typesetting industry. Lorem Ipsum has been the industry's standard dummy text ever since the 1500s</p>
<div class="btn btn-ghost">Learn more</div>
<div class="btn btn-solid" style="left:609px;top:404px;width:210px">Contact us
  <span class="btn-arrow"><svg width="24" height="24" viewBox="0 0 24 24"><path d="M4 12h14M12 5l7 7-7 7" stroke="#fc7d4b" stroke-width="3" fill="none"/></svg></span>
</div>
<div class="swatch" style="top:425px;background:var(--orange)"></div>
<div class="swatch" style="top:472px;background:var(--blue)"></div>
<div class="swatch" style="top:518px;background:#3a3e44"></div>

<!-- welcome -->
<h2 class="abs welcome-title heading">Welcome to <span class="accent">Zorbo</span></h2>
<p class="abs welcome-text">Lorem Ipsum is simply dummy text of the printing and typesetting industry. Lorem Ipsum has been the industry's standard dummy text ever since the 1500s, when an unknown printer took a galley of type and scrambled it to make a type specimen book. It has survived not only five centuries, but also the leap into electronic typesetting, remaining essentially unchanged. It was popularised in the 1960s with the release of Letraset sheets containing Lorem Ipsum passages, and more recently with desktop publishing software like Aldus PageMaker including versions of Lorem Ipsum.</p>
<div class="btn btn-solid" style="left:79px;top:999px;width:206px;height:53px;font-size:20px">Learn more
  <span class="btn-arrow" style="width:45px;height:45px"><svg width="22" height="22" viewBox="0 0 24 24"><path d="M4 12h14M12 5l7 7-7 7" stroke="#fc7d4b" stroke-width="3" fill="none"/></svg></span>
</div>
<div class="abs video" role="img" aria-label="Video still of a couple relaxing in beach chairs by the sea" style="background:linear-gradient(180deg,#5aa8dc 0%,#8fc6e8 45%,#3f8cc4 75%,#6a7f8f 100%)"></div>
<div class="abs play"><svg width="54" height="54" viewBox="0 0 54 54"><polygon points="21,15 39,27 21,39" fill="#fff"/></svg></div>

<!-- how it works background -->
<div class="abs how-bg" role="img" aria-label="Resort lagoon and wooden jetty at night with palm trees" style="background:linear-gradient(180deg,#2a3446 0%,#1f2733 40%,#2b2a28 75%,#1c1c1f 100%)"></div>

<!-- benefit -->
<svg class="abs" style="left:0;top:1111px" width="1200" height="650" viewBox="0 1111 1200 650">
  <polygon points="0,1111 1200,1171 1200,1675 0,1750" fill="#fc7d4b"/>
</svg>
<svg class="abs" style="left:0;top:1111px" width="600" height="650" viewBox="0 1111 600 650" role="img" aria-label="Couple of travellers looking at the app on a smartphone">
  <defs>
    <linearGradient id="benGrad" x1="0" y1="0" x2="1" y2="1">
      <stop offset="0" stop-color="#56697a"/>
      <stop offset=".5" stop-color="#3c4f63"/>
      <stop offset="1" stop-color="#59646b"/>
    </linearGradient>
  </defs>
  <polygon points="0,1111 600,1142 600,1680 0,1750" fill="url(#benGrad)"/>
</svg>
<h2 class="abs benefit-title heading">Zorbo <span style="color:var(--white)">Benefit</span></h2>
<ul class="abs benefit-list">
  <li><svg width="22" height="16" viewBox="0 0 22 16"><path d="M2 2l16 6-16 6 4-6z" fill="#fff"/></svg>Increes your guest service speed by 70%</li>
  <li class="mixed"><svg width="22" height="16" viewBox="0 0 22 16"><path d="M2 2l16 6-16 6 4-6z" fill="#fff"/></svg>Optimize &nbsp;70% OF THE WAITER CHOR</li>
  <li><svg width="22" height="16" viewBox="0 0 22 16"><path d="M2 2l16 6-16 6 4-6z" fill="#fff"/></svg>Avoid human error</li>
  <li><svg width="22" height="16" viewBox="0 0 22 16"><path d="M2 2l16 6-16 6 4-6z" fill="#fff"/></svg>Increase your average check value</li>
  <li><svg width="22" height="16" viewBox="0 0 22 16"><path d="M2 2l16 6-16 6 4-6z" fill="#fff"/></svg>Sharpen your offering</li>
  <li><svg width="22" height="16" viewBox="0 0 22 16"><path d="M2 2l16 6-16 6 4-6z" fill="#fff"/></svg>Go fast &amp; green</li>
  <li><svg width="22" height="16" viewBox="0 0 22 16"><path d="M2 2l16 6-16 6 4-6z" fill="#fff"/></svg>Build loyalty</li>
  <li><svg width="22" height="16" viewBox="0 0 22 16"><path d="M2 2l16 6-16 6 4-6z" fill="#fff"/></svg>Achive higher completion rate</li>
  <li><svg width="22" height="16" viewBox="0 0 22 16"><path d="M2 2l16 6-16 6 4-6z" fill="#fff"/></svg>Reach your target group</li>
</ul>

<!-- how it works -->
<h2 class="abs how-title heading">How it <span class="accent">works</span></h2>

<div class="step-box" style="left:397px;top:1852px">
  <svg width="104" height="104" viewBox="0 0 104 104" fill="none" stroke="#fff" stroke-width="4"><path d="M52 14c-12 0-20 9-20 20 0 15 20 36 20 36s20-21 20-36c0-11-8-20-20-20z"/><circle cx="52" cy="34" r="7"/><path d="M30 62l-16 28h76L74 62"/></svg>
</div>
<div class="step-text" style="left:574px;top:1880px"><h3>LOCATE</h3><p>Lorem Ipsum is simply dummy text of the printing and typesetting industry. Lorem Ipsum has been the industry's standard dummy text ever.</p></div>

<div class="step-box" style="left:552px;top:2007px">
  <svg width="104" height="104" viewBox="0 0 104 104" fill="none" stroke="#fff" stroke-width="4"><rect x="14" y="18" width="76" height="62" rx="4"/><path d="M14 32h76"/><circle cx="22" cy="25" r="2" fill="#fff"/><circle cx="30" cy="25" r="2" fill="#fff"/><path d="M48 88V60h-10l14-14 14 14H56v28z"/></svg>
</div>
<div class="step-text right" style="left:268px;top:2028px"><h3>BROWSE</h3><p>Lorem Ipsum is simply dummy text of the printing and typesetting industry. Lorem Ipsum has been the industry's standard dummy text ever.</p></div>

<div class="step-box" style="left:397px;top:2162px">
  <svg width="104" height="104" viewBox="0 0 104 104" fill="none" stroke="#fff" stroke-width="4"><rect x="16" y="30" width="34" height="50" rx="4"/><rect x="54" y="24" width="34" height="50" rx="4"/><path d="M28 72h10M66 66h10"/></svg>
</div>
<div class="step-text" style="left:574px;top:2184px"><h3>ORDER</h3><p>Lorem Ipsum is simply dummy text of the printing and typesetting industry. Lorem Ipsum has been the industry's standard dummy text ever.</p></div>

<div class="step-box" style="left:552px;top:2317px">
  <svg width="104" height="104" viewBox="0 0 104 104" fill="none" stroke="#fff" stroke-width="4"><path d="M20 62a32 32 0 0 1 64 0z"/><circle cx="52" cy="26" r="4"/><path d="M14 62h76M22 78h44l18-10"/></svg>
</div>
<div class="step-text right" style="left:268px;top:2340px"><h3>HELP</h3><p>Lorem Ipsum is simply dummy text of the printing and typesetting industry. Lorem Ipsum has been the industry's standard dummy text ever.</p></div>

<div class="step-box" style="left:397px;top:2477px">
  <svg width="104" height="104" viewBox="0 0 104 104" fill="none" stroke="#fff" stroke-width="4"><rect x="10" y="34" width="74" height="44" rx="3"/><path d="M18 26h74v44"/><circle cx="47" cy="56" r="14"/><text x="47" y="63" text-anchor="middle" font-family="Roboto,sans-serif" font-size="20" font-weight="700" fill="#fff" stroke="none">$</text></svg>
</div>
<div class="step-text" style="left:574px;top:2498px"><h3>PAY</h3><p>Lorem Ipsum is simply dummy text of the printing and typesetting industry. Lorem Ipsum has been the industry's standard dummy text ever.</p></div>

<!-- news -->
<h2 class="abs news-title heading">Latest <span class="accent">News</span></h2>

<article class="news-card" style="left:79px">
  <div class="news-img" role="img" aria-label="Woman in a sun hat relaxing by a swimming pool" style="background:linear-gradient(180deg,#29b8e0,#0f8fc4)"></div>
  <div class="news-date">05<br>Sep</div>
  <h3 class="news-head">Lorem ipsum is simply dummy text of the printing</h3>
  <p class="news-body">Lorem Ipsum is simply dummy text of the printing and typesetting industry.</p>
</article>
<article class="news-card" style="left:433px">
  <div class="news-img" role="img" aria-label="Smartphone paying at a card terminal" style="background:linear-gradient(135deg,#4e5a68,#1f2a36)"></div>
  <div class="news-date">05<br>Sep</div>
  <h3 class="news-head">Lorem ipsum is simply dummy text of the printing</h3>
  <p class="news-body">Lorem Ipsum is simply dummy text of the printing and typesetting industry.</p>
</article>
<article class="news-card" style="left:789px">
  <div class="news-img" role="img" aria-label="Coffee cup on a table beside the sea" style="background:linear-gradient(180deg,#5cb3e0 0%,#3a9ad0 50%,#dad7d0 100%)"></div>
  <div class="news-date">05<br>Sep</div>
  <h3 class="news-head">Lorem ipsum is simply dummy text of the printing</h3>
  <p class="news-body">Lorem Ipsum is simply dummy text of the printing and typesetting industry.</p>
</article>

<!-- footer -->
<footer class="abs footer"></footer>
<h4 class="foot-head" style="left:79px;width:166px">Quick Links</h4>
<ul class="abs foot-links">
  <li>» Home</li><li>» How it works</li><li>» Benefit</li><li>» who we are</li><li>» Faq</li><li>» Contact</li>
</ul>
<div class="divider" style="left:258px"></div>

<h4 class="foot-head" style="left:292px;width:285px">Contact Details</h4>
<div class="contact-row" style="top:3311px">
  <svg width="14" height="20" viewBox="0 0 14 20"><path d="M7 0C3 0 0 3 0 7c0 5 7 13 7 13s7-8 7-13c0-4-3-7-7-7zm0 10a3 3 0 1 1 0-6 3 3 0 0 1 0 6z" fill="#fff"/></svg>
  <span>123 Building Name, Street Name, City,<br>Country - Zipcode</span>
</div>
<div class="contact-row" style="top:3386px">
  <svg width="16" height="18" viewBox="0 0 16 18"><path d="M3 1l3 4-2 2c1 3 3 5 6 6l2-2 4 3-2 3C7 17 0 10 1 3z" fill="#fff"/></svg>
  <span>+971 5 23 47 90 18</span>
</div>
<div class="contact-row" style="top:3440px">
  <svg width="16" height="12" viewBox="0 0 16 12"><rect width="16" height="12" fill="#fff"/><path d="M0 0l8 7 8-7" stroke="#333" stroke-width="1.5" fill="none"/></svg>
  <span>info@zorboapp-mail.com</span>
</div>
<div class="divider" style="left:579px"></div>

<h4 class="foot-head" style="left:607px;width:249px">Quick Inquiry</h4>
<div class="field" style="top:3313px">Name</div>
<div class="field" style="top:3356px">Email</div>
<div class="field" style="top:3396px">Message</div>
<div class="abs submit">SUBMIT</div>

<div class="brand" style="left:884px;top:3318px;font-size:52px;color:var(--white)">
  <span class="brand-dot" style="width:40px;height:40px"></span><span>zorbo</span>
</div>
<div class="social" style="left:922px"></div>
<div class="social" style="left:975px;background:#d84a38"></div>
<div class="social" style="left:1028px;background:#2aa3dc"></div>

<div class="abs copyright">© <b>ZORBO</b> - 2017 . All Rights Reserved.</div>

</body>
</html>
```